Urgent Flyer needed - Term 1 begins

I am looking for a flyer design - double sided half A4 full colour. Bright Sprouts Early Learning Centre is in Dubai and runs a program for children aged from 6 months to 6 years old. Please see our website and Facebook page for more info on the brand and service. www.facebook.com/brightsprouts and www.brightsprouts.example
We are also offering a free class voucher so i thought something creative like a vintage coupon or a golden ticket style design could work well... I also like the idea of something like a happy bunch of kids learning as a background image in black and white and then BRIGHT SPROUTS in our colours with our contact details and then on the reverse side a bit of text, and the free class info...

Industry/Entity Type

Learning

```html
<!DOCTYPE html>
<html lang="en">
<head>
<meta charset="utf-8">
<title>Bright Sprouts Early Learning Centre – Flyer Front</title>
<link rel="stylesheet" href="https://fonts.googleapis.com/css2?family=Sniglet:wght@400;800&display=swap">
<style>
  :root {
    --page-bg: #2e2a28;
    --sky-top: #74b9d0;
    --sky-bottom: #3e8aa7;
    --orange: #f28a2b;
    --teal-dark: #1f6b86;
    --teal-label: #4a8fa6;
    --white: #ffffff;
    --photo-warm: #d9cdbf;
    --photo-cool: #c9d4d8;
    --shadow: rgba(0, 0, 0, 0.35);
  }

  * { box-sizing: border-box; margin: 0; padding: 0; }

  html, body {
    width: 1200px;
    height: 1000px;
    overflow: hidden;
    background: var(--page-bg);
  }

  .flyer {
    position: absolute;
    left: 290px;
    top: 35px;
    width: 620px;
    height: 930px;
    overflow: hidden;
    background: linear-gradient(180deg, var(--sky-top) 0%, var(--sky-bottom) 100%);
    font-family: "Sniglet", "Comic Sans MS", cursive;
    color: var(--white);
  }

  .corner-band {
    position: absolute;
    inset: 0;
    width: 620px;
    height: 930px;
  }

  .brand-card {
    position: absolute;
    left: 40px;
    top: 40px;
    width: 230px;
    height: 270px;
    background: var(--white);
    border-radius: 14px;
    box-shadow: 0 4px 10px var(--shadow);
    display: flex;
    flex-direction: column;
    align-items: center;
    justify-content: center;
    gap: 18px;
    padding: 20px;
    text-align: center;
  }

  .brand-card__dot {
    width: 46px;
    height: 46px;
    border-radius: 50%;
    background: var(--orange);
  }

  .brand-card__name {
    font-weight: 400;
    font-size: 24px;
    line-height: 1.2;
    color: var(--teal-label);
  }

  .headline {
    position: absolute;
    right: 30px;
    top: 55px;
    width: 300px;
    text-align: right;
    font-weight: 400;
    line-height: 1.15;
    white-space: nowrap;
    text-shadow: 0 2px 3px rgba(0, 0, 0, 0.25);
  }

  .headline__brand { display: block; font-size: 40px; margin-bottom: 6px; }
  .headline__line { display: block; font-size: 26px; }
  .headline__line--big { font-size: 32px; }

  .photo {
    position: absolute;
    border: 8px solid var(--white);
    box-shadow: 0 6px 14px var(--shadow);
    z-index: 1;
  }

  .photo--abacus {
    left: 55px;
    top: 390px;
    width: 310px;
    height: 225px;
    background: linear-gradient(135deg, var(--photo-cool), var(--photo-warm));
  }

  .photo--playroom {
    left: 285px;
    top: 520px;
    width: 310px;
    height: 225px;
    z-index: 2;
    background: linear-gradient(135deg, #e9e6e1, #c98a6d);
  }

  .flower-border {
    position: absolute;
    left: 0;
    bottom: 0;
    width: 620px;
    height: 190px;
    background: radial-gradient(ellipse 70% 100% at 75% 100%, rgba(255, 255, 255, 0.45) 0%, rgba(255, 255, 255, 0) 75%);
  }

  .age-badge {
    position: absolute;
    left: 30px;
    top: 775px;
    width: 245px;
    height: 90px;
    z-index: 3;
  }

  .age-badge__shadow {
    position: absolute;
    left: 18px;
    top: 18px;
    width: 245px;
    height: 90px;
    background: var(--teal-dark);
  }

  .age-badge__box {
    position: absolute;
    inset: 0;
    padding: 0 14px;
    background: var(--orange);
    display: flex;
    flex-direction: column;
    justify-content: center;
    align-items: center;
    font-weight: 400;
    font-size: 25px;
    line-height: 1.1;
    white-space: nowrap;
    text-shadow: 0 2px 2px rgba(0, 0, 0, 0.2);
  }
</style>
</head>
<body>
  <main class="flyer">
    <svg class="corner-band" viewBox="0 0 620 930" aria-hidden="true">
      <polygon points="0,0 530,0 0,270" fill="var(--orange)"/>
      <polygon points="530,0 548,0 0,279 0,270" fill="var(--white)"/>
    </svg>

    <div class="brand-card">
      <span class="brand-card__dot"></span>
      <p class="brand-card__name">Bright Sprouts<br>Early Learning Centre</p>
    </div>

    <h1 class="headline">
      <span class="headline__brand">Bright Sprouts</span>
      <span class="headline__line">Early Learning</span>
      <span class="headline__line">Centre offers</span>
      <span class="headline__line">special accelerated</span>
      <span class="headline__line headline__line--big">learning classes</span>
      <span class="headline__line">for your child</span>
    </h1>

    <div class="flower-border" role="img" aria-label="Decorative border of white paper flowers with small orange dots"></div>

    <div class="photo photo--abacus" role="img" aria-label="Photo of a young boy working with a colourful abacus at a desk"></div>
    <div class="photo photo--playroom" role="img" aria-label="Photo of two teachers playing with a baby on the floor of a bright playroom"></div>

    <div class="age-badge">
      <div class="age-badge__shadow"></div>
      <p class="age-badge__box"><span>Age – 6 months</span><span>to 6 years old</span></p>
    </div>
  </main>
</body>
</html>
```